need a Flyer for Plush Toy company

Need a Flyer for Plush Toy company ,

I upload a file for TEXT

Target Market(s)

Toys wholesalers , Supermarket

Industry/Entity Type

Toy Store

Colors
000000
ec1f27
c4c4c4

Requirements
Must have
• I have up loaded 3 files
• 1. Logo Registered Brand
• 2. customer's design in drawing
• 3. our ready samples based on Design
Nice to have
• happy kids in Nature ,
• happy kids in Ski ,
• different color Kids ,
• Multi culture concept

```html
<!DOCTYPE html>
<html lang="en">
<head>
<meta charset="utf-8">
<title>Lumo Kade – Plush Toys Flyer</title>
<link rel="stylesheet" href="https://fonts.googleapis.com/css2?family=Oswald:wght@600;700&family=Open+Sans:wght@600;700&family=Arimo:wght@400;700&display=swap">
<style>
  :root {
    --brand-red: #ec1f27;
    --ink: #000000;
    --panel-black: #1e1e1e;
    --soft-grey: #c4c4c4;
    --circle-grey: #e4e4ea;
    --paper: #ffffff;
    --backdrop: #ececec;
  }
  * { box-sizing: border-box; margin: 0; padding: 0; }
  html, body { width: 1200px; height: 1200px; overflow: hidden; background: var(--backdrop); }
  .flyer {
    position: absolute; left: 190px; top: 20px;
    width: 820px; height: 1160px;
    background: var(--paper);
    overflow: hidden;
    font-family: "Arimo", Arial, sans-serif;
    color: var(--ink);
    box-shadow: 0 6px 24px rgba(0,0,0,.18);
  }
  .flyer > * { position: absolute; }

  .brand-mark {
    left: 0; width: 820px; top: 150px;
    display: flex; justify-content: center; align-items: center; gap: 14px;
    font-family: "Open Sans", sans-serif; font-weight: 700;
    font-size: 40px; color: var(--brand-red);
  }
  .brand-mark .dot { width: 26px; height: 26px; border-radius: 50%; background: var(--brand-red); }

  .red-band { left: 0; top: 0; width: 820px; height: 1160px; }

  .toy-circle {
    left: 520px; top: 200px; width: 290px; height: 290px; border-radius: 50%;
    border: 6px solid #fff;
    background: radial-gradient(circle at 50% 55%, #f0d8e6 0%, #e6e0f2 28%, var(--circle-grey) 60%);
  }

  .headline {
    left: 36px; top: 272px; width: 480px;
    font-family: "Oswald", sans-serif; font-weight: 700;
    color: #fff; line-height: 1.2; transform: rotate(-1.5deg);
  }
  .headline .name { font-size: 38px; }
  .headline .sub { font-size: 28px; }
  .headline .line2 { font-size: 34px; }

  .taglines {
    left: 40px; top: 378px;
    font-family: "Open Sans", sans-serif; font-weight: 700;
    font-size: 20px; color: #fff; line-height: 1.55;
    transform: rotate(-1.5deg);
  }

  .kids-card {
    left: 66px; top: 455px; width: 305px; height: 285px;
    border-radius: 10px; overflow: hidden;
    background: var(--panel-black);
    box-shadow: 0 4px 10px rgba(0,0,0,.3);
    transform: rotate(-1.5deg);
  }
  .kids-card .photo {
    height: 130px;
    background: linear-gradient(180deg, #6f9a3c 0%, #8fb454 45%, #c58a8e 80%, var(--panel-black) 100%);
  }
  .kids-card .copy { padding: 6px 14px; color: #fff; font-size: 13.5px; line-height: 1.4; }
  .kids-card .copy p + p { margin-top: 8px; font-size: 12.5px; }

  .about {
    left: 430px; top: 570px; width: 345px;
    font-size: 13.5px; line-height: 1.4; transform: rotate(-1.5deg);
  }
  .about p + p { margin-top: 14px; text-align: justify; }
  .about .address {
    margin-top: 14px; font-family: "Open Sans", sans-serif; font-weight: 700; font-size: 16px;
  }

  .contact {
    left: 92px; top: 752px; font-size: 14.5px; line-height: 1.6;
    transform: rotate(-1.5deg);
  }
  .contact h2 { font-size: 19px; font-weight: 700; margin-bottom: 2px; }
  .contact .mail { font-weight: 700; font-size: 16px; display: flex; align-items: center; gap: 6px; }

  .bank-panel {
    left: 0; top: 930px; width: 470px; height: 190px; background: var(--panel-black);
  }
  .bank-tab {
    left: 170px; top: 898px; width: 165px; height: 40px;
    background: var(--brand-red); border-radius: 16px 16px 0 0;
    color: #fff; font-family: "Open Sans", sans-serif; font-weight: 700; font-size: 22px;
    text-align: center; line-height: 42px; transform: rotate(-1.5deg);
  }
  .bank-details {
    left: 100px; top: 942px; color: #fff; font-size: 14.5px; line-height: 1.85;
    transform: rotate(-1.5deg);
  }
  .sofa-art {
    left: 100px; top: 1035px; width: 310px; height: 85px; border-radius: 10px 10px 4px 4px;
    background: linear-gradient(180deg, #f0e8e0 0%, #c8dcbf 40%, #93c6a1 100%);
  }

  .kids-art {
    left: 475px; top: 800px; width: 335px; height: 310px; border-radius: 40% 40% 8px 8px;
    background: radial-gradient(ellipse at 50% 45%, #fbd7a8 0%, #f7a95a 30%, #f6e7f0 65%, rgba(255,255,255,0) 80%);
  }
  .bottom-strip { left: 0; top: 1120px; width: 820px; height: 40px; background: var(--brand-red); }
</style>
</head>
<body>
<main class="flyer">
  <div class="brand-mark"><span class="dot"></span><span>Plushwharf</span></div>

  <svg class="red-band" viewBox="0 0 820 1160" aria-hidden="true">
    <path d="M0 262 L610 246 L610 490 C520 496 450 512 380 525 L0 560 Z" fill="var(--brand-red)"/>
  </svg>

  <div class="toy-circle" role="img" aria-label="Photo of a row of pastel plush toy samples: rabbit, lion, dolphin, bird and chick"></div>

  <h1 class="headline">
    <span class="name">LUMO KADE,</span> <span class="sub">einzelunternehmen /</span><br>
    <span class="line2">Family business</span>
  </h1>
  <div class="taglines">
    <p>Innovative Developer&nbsp; for Plush Toys</p>
    <p>International Trader for Toys</p>
  </div>

  <section class="kids-card">
    <div class="photo" role="img" aria-label="Photo of three happy girls running on green grass"></div>
    <div class="copy">
      <p>100 Yen = 0.90 USD &nbsp;, Our products can meet strictest Quality Control , but are with extremely Low Price to fit for Japanese Dollar Shop as well as his overseas Store around the world.</p>
      <p>Of course our products are fit for Premium Store too.</p>
    </div>
  </section>

  <section class="about">
    <p>We live and work in Rheinfeld near to Cologne Germany.<br>We speak German and English.</p>
    <p>The toys are made in China, we are small family business, but we are professional in Plush toys business , right now we have successfully launched Projects with a huge Japanese 100 Yen Chain Store. Here in Flyer we show a Sample project.</p>
    <p class="address">Lindenweg 8, 50100 Rheinfeld Germany</p>
  </section>

  <section class="contact">
    <h2>Contact us</h2>
    <p>Fon &nbsp;&nbsp;+49 (0) &nbsp;2200- 410 1100</p>
    <p>Fax &nbsp;&nbsp;+49 (0) &nbsp;2200- 410 1101</p>
    <p>Mobile : &nbsp;+49 (0) 170 0000 123</p>
    <p>Ust-IdNr./VAT No. DE000111222</p>
    <p class="mail">
      <svg width="20" height="14" viewBox="0 0 20 14" aria-hidden="true"><rect x="0.5" y="0.5" width="19" height="13" fill="var(--brand-red)"/><path d="M1 1 L10 8 L19 1" stroke="#fff" stroke-width="1.6" fill="none"/></svg>
      hello@lumokade.de
    </p>
  </section>

  <div class="bank-panel"></div>
  <div class="bank-tab">Bank Details</div>
  <section class="bank-details">
    <p>Kontoinhaber/Account Holder: &nbsp;Mira Holt</p>
    <p>IBAN: &nbsp;DE00 1234 5678 9012 3456 00</p>
    <p>BIC : ABCDDEFF000</p>
  </section>
  <div class="sofa-art" role="img" aria-label="Drawing of a green sofa with six cute plush toy characters sitting on it"></div>

  <div class="kids-art" role="img" aria-label="Illustration of four cheerful children of different cultures jumping with joy"></div>
  <div class="bottom-strip"></div>
</main>
</body>
</html>
```